Construction Company

I'm a new construction company called Kelden Construction. I want my card to look simple and clean. I have provided a sample of what I want the front to look like (Kelden_Card.jpeg) and a back ground for the back of the (Kelden_Card_Background.jpeg) - the background can be faded so my name and other information is more prominent.
Construction

```html
<!DOCTYPE html>
<html lang="en">
<head>
<meta charset="utf-8">
<title>Kelden Construction – Business Card</title>
<link rel="stylesheet" href="https://fonts.googleapis.com/css2?family=Mulish:wght@400;500&display=swap">
<style>
  :root {
    --stage: #1f1f1f;
    --card-light: #ffffff;
    --plan-tone: #ececec;
    --accent: #e08a1a;
    --ink: #2b2b2b;
    --card-dark: #3f3a2c;
    --icon-fg: #ffffff;
  }
  * { margin: 0; padding: 0; box-sizing: border-box; }
  html, body { width: 1200px; height: 900px; overflow: hidden; }
  body {
    background: var(--stage);
    font-family: "Mulish", "Helvetica Neue", Arial, sans-serif;
    position: relative;
  }
  .card {
    position: absolute;
    left: 355px;
    width: 487px;
    height: 279px;
    overflow: hidden;
  }
  .card--front { top: 153px; background: var(--card-light); }
  .card--back { top: 463px; background: var(--card-dark); }

  .floor-plan {
    position: absolute;
    left: 120px; top: 0;
    width: 367px; height: 279px;
    background: linear-gradient(100deg, rgba(236,236,236,0) 0%, var(--plan-tone) 35%, #e4e4e4 100%);
  }
  .holder-name {
    position: absolute;
    left: 28px; top: 38px;
    font-size: 24px; font-weight: 500;
    color: var(--accent);
    letter-spacing: 0.3px;
  }
  .holder-role {
    position: absolute;
    left: 28px; top: 69px;
    font-size: 13px; color: var(--ink);
    letter-spacing: 0.6px;
  }
  .address {
    position: absolute;
    left: 28px; top: 113px;
    font-size: 13.5px; line-height: 20px;
    color: var(--ink); font-style: normal;
  }
  .contact-list {
    position: absolute;
    left: 28px; top: 173px;
    list-style: none;
  }
  .contact-item {
    display: flex; align-items: center;
    height: 27px;
    font-size: 14px; color: var(--ink);
  }
  .contact-icon { width: 22px; height: 22px; margin-right: 13px; flex: none; }
  .contact-item .domain { color: var(--accent); }

  .license-tab {
    position: absolute;
    right: 0; bottom: 0;
    width: 176px; height: 27px;
  }
  .license-tab svg { position: absolute; left: 0; top: 0; }
  .license-number {
    position: absolute;
    left: 27px; top: 6px;
    font-size: 12.5px; letter-spacing: 1px;
    color: var(--ink);
  }

  .brand-name {
    position: absolute;
    left: 0; right: 0; top: 112px;
    text-align: center;
    font-size: 44px; font-weight: 400;
    color: var(--accent);
    letter-spacing: 0.5px;
  }
</style>
</head>
<body>
  <section class="card card--front" aria-label="Card front">
    <div class="floor-plan" role="img" aria-label="Faded architectural floor plan background"></div>

    <h1 class="holder-name">Mateo Ferrante</h1>
    <p class="holder-role">OWNER</p>

    <address class="address">2417 Cedar Ridge Lane<br>Marlow, CA 93811</address>

    <ul class="contact-list">
      <li class="contact-item">
        <svg class="contact-icon" viewBox="0 0 22 22" aria-hidden="true">
          <circle cx="11" cy="11" r="11" fill="var(--accent)"/>
          <rect x="7.5" y="5" width="7" height="12" rx="1.2" fill="none" stroke="var(--icon-fg)" stroke-width="1.4"/>
          <rect x="9" y="7" width="4" height="7" fill="var(--icon-fg)"/>
        </svg>
        555.214.7380
      </li>
      <li class="contact-item">
        <svg class="contact-icon" viewBox="0 0 22 22" aria-hidden="true">
          <circle cx="11" cy="11" r="11" fill="var(--accent)"/>
          <rect x="5.5" y="7" width="11" height="8" fill="var(--icon-fg)"/>
          <path d="M5.5 7 L11 11.5 L16.5 7" fill="none" stroke="var(--accent)" stroke-width="1.2"/>
        </svg>
        mateo@keldenconstruction.com
      </li>
      <li class="contact-item">
        <svg class="contact-icon" viewBox="0 0 22 22" aria-hidden="true">
          <circle cx="11" cy="11" r="11" fill="var(--accent)"/>
          <circle cx="11" cy="11" r="5.5" fill="none" stroke="var(--icon-fg)" stroke-width="1.4"/>
          <ellipse cx="11" cy="11" rx="2.3" ry="5.5" fill="none" stroke="var(--icon-fg)" stroke-width="1.1"/>
          <line x1="5.5" y1="11" x2="16.5" y2="11" stroke="var(--icon-fg)" stroke-width="1.1"/>
        </svg>
        <span>www.<span class="domain">keldenconstruction</span>.com</span>
      </li>
    </ul>

    <div class="license-tab">
      <svg width="176" height="27" viewBox="0 0 176 27" aria-hidden="true">
        <rect x="10" y="2" width="166" height="25" fill="var(--card-light)"/>
        <path d="M1 27 C 3 10, 10 2, 24 2 L 176 2" fill="none" stroke="var(--accent)" stroke-width="2"/>
      </svg>
      <span class="license-number">CONTRACT #471592</span>
    </div>
  </section>

  <section class="card card--back" aria-label="Card back">
    <p class="brand-name">Kelden Construction</p>
  </section>
</body>
</html>
```